Auto Bodyshop Personal Injury Clients Focus

We are a busy body shop that focuses on personal injury work and custom work.

Please review website. We need marketing material. Outside of the basic body shop material we want to add a few points that make us stand out.

https://www.ratemyspot.example/biz/durvin-collision-los-angeles-2

https://www.snapgrid.example/durvincollision/

http://www.durvincollision.example/

Please gather material from our website. Stay consistent with color and modern design and incorporate with better working the following points.

1. Can pick up and tow cars from any geographic location
2. Provide rentals and will drop off and pick them up
3. Can work on a lien basis
4. Handle Property damage as a curtesy
5. have huge storage capabilities
6. Quick turn around on estimates
7. Offer Presentation Packages for litigation purposes.

I want to give designers more time

Attorneys

Personal Injury, Auto Body Shop

Must have
• Tri fold, double sided, USA letter format
Nice to have
• As much information as possible but on the front page the important points I added but maybe bettter more professional wording

```html
<!DOCTYPE html>
<html lang="en">
<head>
<meta charset="utf-8">
<title>Durvin Collision – Tri-fold Brochure</title>
<link rel="stylesheet" href="https://fonts.googleapis.com/css2?family=Krona+One&family=Titillium+Web:ital,wght@0,400;0,600;0,700;1,400&display=swap">
<style>
:root{
  --yellow:#f4c531;
  --yellow-deep:#e3ad14;
  --ink:#0d0d0d;
  --panel:#151515;
  --white:#ffffff;
  --grey:#8a8a8a;
  --grey-light:#e9e9e9;
  --stage:#e3e5e8;
  --rule:#4a4a4a;
}
*{box-sizing:border-box;margin:0;padding:0}
html,body{width:1200px;height:2458px;overflow:hidden;background:var(--stage)}
body{font-family:"Titillium Web",Arial,sans-serif;color:var(--white)}
.brochure{position:absolute;left:40px;top:796px;width:1120px;height:866px;background:var(--ink);overflow:hidden;box-shadow:0 10px 30px rgba(0,0,0,.25)}
.artwork{position:absolute;inset:0;width:1120px;height:866px}

/* panel 1 – key points */
.key-points-label{position:absolute;left:-182px;top:560px;width:420px;height:52px;line-height:52px;text-align:center;transform:rotate(-90deg);font-family:"Krona One",sans-serif;font-size:48px;letter-spacing:2px;color:#242424;white-space:nowrap}
.key-points{position:absolute;left:70px;top:322px;width:290px;list-style:none}
.key-points li{display:flex;align-items:center;height:68px;border-bottom:1px dashed var(--rule)}
.key-points li:last-child{border-bottom:none}
.key-points svg{flex:none;width:52px;height:56px;margin-right:23px}
.key-points span{font-size:14.5px;line-height:18px;font-weight:600;color:var(--white)}

/* panel 2 – about / contact */
.ribbon{position:absolute;left:437px;width:246px;height:36px;display:flex;align-items:center;justify-content:space-between;padding:0 16px;font-family:"Krona One",sans-serif;font-size:19px;letter-spacing:1px}
.ribbon::before{content:"";position:absolute;inset:0;transform:skewX(-18deg);z-index:-1}
.ribbon .dot{width:11px;height:11px;border-radius:50%;border:2px solid currentColor;position:relative}
.ribbon .dot::after{content:"";position:absolute;left:50%;top:50%;width:5px;height:1.5px;background:currentColor;transform:translate(-50%,-50%)}
.ribbon-about{top:42px;color:var(--white);z-index:1}
.ribbon-about::before{background:var(--ink)}
.ribbon-contact{top:582px;color:var(--ink);z-index:1}
.ribbon-contact::before{background:linear-gradient(180deg,#fff,#cfcfcf)}
.about-copy{position:absolute;left:405px;top:106px;width:310px;text-align:center;color:#1a1a1a;font-size:14.3px;line-height:18.5px}
.about-copy p+p{margin-top:18px}
.about-copy strong{font-weight:700}
.contact-icons{position:absolute;left:512px;top:637px;display:flex;gap:5px}
.contact-icons svg{width:22px;height:22px}
.contact-copy{position:absolute;left:389px;top:664px;width:342px;text-align:center;font-size:14.3px;line-height:18.5px}

/* panel 3 – cover */
.brand{position:absolute;left:746px;top:78px;width:374px;display:flex;align-items:center;justify-content:center;gap:10px;font-weight:600;font-size:25px;letter-spacing:1px;color:var(--white);white-space:nowrap}
.brand i{display:block;width:18px;height:18px;background:var(--white)}
.headline{position:absolute;left:746px;top:596px;width:374px;text-align:center;font-family:"Krona One",sans-serif;line-height:1}
.headline .line-1{display:block;font-size:44px;color:var(--yellow)}
.headline .line-2{display:block;margin-top:12px;font-size:27px;color:var(--white)}
.tagline{position:absolute;left:746px;top:700px;width:374px;text-align:center;font-style:italic;font-size:18.5px;line-height:23px;color:#ececec}

/* footer */
.footer{position:absolute;top:812px;height:36px;width:373px;display:flex;align-items:center;justify-content:space-between;padding:0 12px;background:linear-gradient(180deg,#f4f4f4,#c9c9c9);color:var(--ink);font-weight:700;font-size:17px;letter-spacing:.8px}
.footer .dot{width:12px;height:12px;border-radius:50%;border:1.5px solid #333;position:relative}
.footer .dot::after{content:"";position:absolute;left:50%;top:50%;width:6px;height:1.5px;background:#333;transform:translate(-50%,-50%)}
.footer-1{left:0}.footer-2{left:373px}.footer-3{left:747px}
</style>
</head>
<body>
<main class="brochure">
  <svg class="artwork" viewBox="0 0 1120 866">
    <defs>
      <radialGradient id="stone" cx="50%" cy="50%" r="70%">
        <stop offset="0" stop-color="#1c1c1c"/><stop offset="1" stop-color="#080808"/>
      </radialGradient>
      <linearGradient id="polishTone" x1="0" y1="0" x2="1" y2="1">
        <stop offset="0" stop-color="#9aa3ab"/><stop offset=".45" stop-color="#2d3a45"/><stop offset="1" stop-color="#0f151b"/>
      </linearGradient>
      <linearGradient id="paintTone" x1="0" y1="0" x2="1" y2="1">
        <stop offset="0" stop-color="#c21a12"/><stop offset=".45" stop-color="#f2b928"/><stop offset=".7" stop-color="#b8140e"/><stop offset="1" stop-color="#5a0c08"/>
      </linearGradient>
      <linearGradient id="garageTone" x1="0" y1="0" x2="1" y2="1">
        <stop offset="0" stop-color="#6d7883"/><stop offset=".5" stop-color="#3a4552"/><stop offset="1" stop-color="#1b2027"/>
      </linearGradient>
    </defs>
    <rect width="1120" height="866" fill="url(#stone)"/>

    <g role="img" aria-label="Photo: gloved hands polishing a dark car panel with a rotary buffer">
      <polygon points="0,0 373,0 373,296 188,215 0,302" fill="url(#polishTone)"/>
    </g>
    <polygon points="0,318 0,302 188,215 373,296 373,312 188,231" fill="#ffffff"/>
    <polygon points="0,318 62,290 66,300 0,330" fill="#5a5a5a"/>

    <polygon points="373,0 746,0 746,490 373,296" fill="var(--yellow)"/>
    <polygon points="373,296 746,490 746,506 373,312" fill="#ffffff"/>

    <polygon points="560,294 666,355 666,479 560,540 454,479 454,355" fill="#ffffff"/>
    <polygon points="560,302 659,359 659,475 560,532 461,475 461,359" fill="#6a6a6a"/>
    <g role="img" aria-label="Photo: dent repair tool pressed against glossy red and yellow car paint">
      <polygon points="560,309 653,363 653,471 560,525 467,471 467,363" fill="url(#paintTone)"/>
    </g>

    <polygon points="746,280 746,250 830,205 880,212" fill="var(--yellow)"/>
    <polygon points="746,258 936,152 1120,240 1120,260 936,168 746,274" fill="#ffffff"/>
    <g role="img" aria-label="Photo: technician crouching beside a car fitting a wheel in a body shop">
      <polygon points="746,274 936,168 1120,260 1120,495 936,553 746,445" fill="url(#garageTone)"/>
    </g>
    <polygon points="746,445 936,553 1120,495 1120,511 936,569 746,461" fill="#ffffff"/>
    <polygon points="1060,540 1120,520 1120,532 1068,552" fill="#5a5a5a"/>
    <polygon points="1070,160 1120,184 1120,196 1078,176" fill="#5a5a5a"/>

    <line x1="373" y1="0" x2="373" y2="866" stroke="#000" stroke-opacity=".4"/>
    <line x1="746" y1="0" x2="746" y2="866" stroke="#000" stroke-opacity=".4"/>
  </svg>

  <!-- Panel 1 -->
  <div class="key-points-label">KEY POINTS</div>
  <ul class="key-points">
    <li>
      <svg viewBox="0 0 52 56"><polygon points="26,1 51,15 51,41 26,55 1,41 1,15" fill="var(--yellow)"/>
        <path d="M12 33V24h14v9zM26 27h6l5 4v2h-11z" fill="var(--ink)"/><circle cx="17" cy="35" r="3" fill="var(--ink)"/><circle cx="33" cy="35" r="3" fill="var(--ink)"/><path d="M20 24l8-7" stroke="var(--ink)" stroke-width="2"/></svg>
      <span>Can pick up and tow cars from<br>any geographic location</span>
    </li>
    <li>
      <svg viewBox="0 0 52 56"><polygon points="26,1 51,15 51,41 26,55 1,41 1,15" fill="var(--yellow)"/>
        <path d="M15 36v-6l3-6h16l3 6v6z" fill="var(--ink)"/><circle cx="19" cy="32" r="1.6" fill="var(--yellow)"/><circle cx="33" cy="32" r="1.6" fill="var(--yellow)"/><path d="M26 12a4 4 0 0 1 4 4c0 3-4 6-4 6s-4-3-4-6a4 4 0 0 1 4-4z" fill="var(--ink)"/></svg>
      <span>Provide rentals and will drop<br>off and pick them up</span>
    </li>
    <li>
      <svg viewBox="0 0 52 56"><polygon points="26,1 51,15 51,41 26,55 1,41 1,15" fill="var(--yellow)"/>
        <rect x="13" y="22" width="14" height="9" rx="4.5" fill="none" stroke="var(--ink)" stroke-width="3" transform="rotate(-40 20 26)"/><rect x="25" y="26" width="14" height="9" rx="4.5" fill="none" stroke="var(--ink)" stroke-width="3" transform="rotate(-40 32 30)"/></svg>
      <span>Can work on a lien basis</span>
    </li>
    <li>
      <svg viewBox="0 0 52 56"><polygon points="26,1 51,15 51,41 26,55 1,41 1,15" fill="var(--yellow)"/>
        <path d="M14 27l12-10 12 10v11H14z" fill="var(--ink)"/><rect x="22" y="30" width="7" height="8" fill="var(--yellow)"/></svg>
      <span>Handle Property damage<br>as a curtesy</span>
    </li>
    <li>
      <svg viewBox="0 0 52 56"><polygon points="26,1 51,15 51,41 26,55 1,41 1,15" fill="var(--yellow)"/>
        <path d="M13 24l13-8 13 8v14H13z" fill="var(--ink)"/><rect x="19" y="27" width="6" height="5" fill="var(--yellow)"/><rect x="27" y="27" width="6" height="5" fill="var(--yellow)"/><rect x="23" y="33" width="6" height="5" fill="var(--yellow)"/></svg>
      <span>Have huge storage capabilities</span>
    </li>
    <li>
      <svg viewBox="0 0 52 56"><polygon points="26,1 51,15 51,41 26,55 1,41 1,15" fill="var(--yellow)"/>
        <circle cx="26" cy="30" r="10" fill="none" stroke="var(--ink)" stroke-width="3"/><rect x="23" y="15" width="6" height="3" fill="var(--ink)"/><path d="M26 30v-6M26 30l4 3" stroke="var(--ink)" stroke-width="2.5"/></svg>
      <span>Quick turn around on estimates</span>
    </li>
    <li>
      <svg viewBox="0 0 52 56"><polygon points="26,1 51,15 51,41 26,55 1,41 1,15" fill="var(--yellow)"/>
        <rect x="20" y="17" width="12" height="9" fill="var(--ink)"/><rect x="13" y="28" width="12" height="10" fill="var(--ink)"/><rect x="27" y="28" width="12" height="10" fill="var(--ink)"/></svg>
      <span>Offer Presentation Packages<br>for litigation purposes.</span>
    </li>
  </ul>

  <!-- Panel 2 -->
  <div class="ribbon ribbon-about"><i class="dot"></i>ABOUT US<i class="dot"></i></div>
  <div class="about-copy">
    <p><strong>Durvin Collision</strong> has been servicing customers since 1984. We are committed to providing industry leading service and quality. Worry free claims processing from start to finish.</p>
    <p>Durvin Collision has had a long history of servicing the Marlow Heights, Cedar Bend, Lindell Park, Ashford, Quarry Glen, Westbrook Village and Halden communities.</p>
  </div>
  <div class="ribbon ribbon-contact"><i class="dot"></i>CONTACT US<i class="dot"></i></div>
  <div class="contact-icons">
    <svg viewBox="0 0 22 22"><circle cx="11" cy="11" r="11" fill="var(--yellow)"/><path d="M11 5a4 4 0 0 1 4 4c0 3-4 8-4 8s-4-5-4-8a4 4 0 0 1 4-4z" fill="var(--ink)"/><circle cx="11" cy="9" r="1.5" fill="var(--yellow)"/></svg>
    <svg viewBox="0 0 22 22"><circle cx="11" cy="11" r="11" fill="var(--yellow)"/><path d="M7 6l3 0 1 3-2 1.5a8 8 0 0 0 3 3L14 12l3 1v3c-6 0-10-4-10-10z" fill="var(--ink)"/></svg>
    <svg viewBox="0 0 22 22"><circle cx="11" cy="11" r="11" fill="var(--yellow)"/><circle cx="11" cy="11" r="6" fill="none" stroke="var(--ink)" stroke-width="2"/><path d="M11 8v3h3" stroke="var(--ink)" stroke-width="1.8" fill="none"/></svg>
    <svg viewBox="0 0 22 22"><circle cx="11" cy="11" r="11" fill="var(--yellow)"/><circle cx="11" cy="11" r="6" fill="none" stroke="var(--ink)" stroke-width="1.6"/><ellipse cx="11" cy="11" rx="2.6" ry="6" fill="none" stroke="var(--ink)" stroke-width="1.4"/><path d="M5 11h12" stroke="var(--ink)" stroke-width="1.4"/></svg>
  </div>
  <div class="contact-copy">
    2150 Ardmore Ave.,<br>
    Marlow Heights, CA 90418, USA<br>
    Free Consultations<br>
    +1 818-555-0147<br>
    Mon-Fri 7:30 a.m. to 5:30 p.m.<br>
    Sat. 9:00 a.m. to 1:00 p.m. Sunday Closed
  </div>

  <!-- Panel 3 -->
  <div class="brand"><i></i>DURVIN COLLISION</div>
  <h1 class="headline"><span class="line-1">DURVIN</span><span class="line-2">COLLISION</span></h1>
  <p class="tagline">We are a busy body shop that<br>focuses on personal injury<br>work and custom work</p>

  <div class="footer footer-1"><i class="dot"></i>www.durvincollision.example<i class="dot"></i></div>
  <div class="footer footer-2"><i class="dot"></i>www.durvincollision.example<i class="dot"></i></div>
  <div class="footer footer-3"><i class="dot"></i>www.durvincollision.example<i class="dot"></i></div>
</main>
</body>
</html>
```